Number of Website Pages Need Designing

I currently have a website design homepage already created, however I am looking for experience designer who can design a page for each of internal pages below which we can use to create the live design. The pages that require a design are:
Page 1- Contact us
Page 2 - About us
Page 3 - Blog
Page 4 - News
Page 5 - Product page, ie fleet insurance
Page 6 - Affiliate / Partners
Page 7 - Brokers page - You could create a page for this one from the information from this YouTube video: https://www.vidorama-example.net/watch?v=Qx4Lm8TzWp2
The design you create need to work with the same site colours, brand, font, look and feel of the site design attached,
You will need to cut and past the header and footer onto your designs so we can see the design fully
The link to our demo site is: https://snip-example.io/7RtKvNa
Please let us see your best designs
Any questions please us us know
Thank you

```html
<!DOCTYPE html>
<html lang="en">
<head>
<meta charset="utf-8">
<title>About Us – Corvanta</title>
<link href="https://fonts.googleapis.com/css2?family=Outfit:wght@400;600;700;800&family=Poppins:wght@300;400;500;600&display=swap" rel="stylesheet">
<style>
:root{
  --navy:#0b2a43;
  --navy-deep:#08223a;
  --green:#22c074;
  --mint:#e9fbf3;
  --team:#b9decd;
  --ink:#0d2236;
  --white:#ffffff;
}
*{margin:0;padding:0;box-sizing:border-box}
html,body{width:1200px;height:3371px;overflow:hidden}
body{font-family:"Poppins",sans-serif;color:var(--ink);background:var(--white);position:relative}
.abs{position:absolute}
.head{font-family:"Outfit",sans-serif;font-weight:800}
.accent{color:var(--green)}
.rule{position:absolute;height:3px;background:var(--green);width:56px}

/* header + hero */
.hero{position:absolute;left:0;top:0;width:1200px;height:455px;background:var(--navy)}
.hero-wave{position:absolute;left:0;top:290px;width:1200px;height:165px;
  background:radial-gradient(ellipse at 50% 45%,rgba(34,192,116,.35),rgba(11,42,67,0) 70%)}
.brand{font-family:"Poppins",sans-serif;font-weight:500;color:var(--white);font-size:27px;display:flex;align-items:center;gap:8px}
.brand i{display:block;width:26px;height:26px;border-radius:50%;background:var(--green)}
.nav{position:absolute;top:38px;font-size:13.5px;color:var(--white);font-weight:500}
.nav span{position:absolute;white-space:nowrap}
.cta{position:absolute;left:807px;top:38px;color:var(--white);font-family:"Outfit",sans-serif;font-weight:700;font-size:14px}
.login{position:absolute;left:957px;top:31px;width:93px;height:34px;border-radius:17px;background:var(--green);color:var(--navy);font-weight:600;font-size:14px;display:flex;align-items:center;justify-content:center}
.hero h1{position:absolute;left:0;width:1200px;top:140px;text-align:center;font-size:50px;color:var(--white)}
.hero p{position:absolute;left:0;width:1200px;top:214px;text-align:center;font-size:15.5px;line-height:26px;color:var(--white)}

/* about */
.about h2{left:148px;top:500px;font-size:37px}
.about .body{left:148px;top:597px;width:555px;font-size:12.4px;line-height:17.3px;text-align:justify}
.card{position:absolute;top:798px;width:266px;height:208px;background:var(--mint);border-radius:14px}
.card h3{position:absolute;left:24px;top:60px;font-family:"Outfit",sans-serif;font-weight:700;font-size:22px}
.card p{position:absolute;left:24px;top:96px;width:226px;font-size:11.5px;line-height:17px}
.card svg{position:absolute;right:24px;top:20px}
.mark{left:757px;top:540px;width:290px;height:460px;border-radius:40px;background:linear-gradient(160deg,var(--mint),#c9f0de)}

/* values */
.values{position:absolute;left:0;top:1067px;width:1200px;height:419px;background:var(--navy)}
.values h2{position:absolute;width:1200px;top:50px;text-align:center;color:var(--white);font-size:37px}
.value{position:absolute;top:166px;width:190px;text-align:center;color:var(--white)}
.value .ic{width:68px;height:68px;border-radius:50%;background:var(--green);margin:0 auto;display:flex;align-items:center;justify-content:center}
.value h3{font-family:"Outfit",sans-serif;font-weight:700;font-size:16.5px;margin-top:28px}
.value p{font-size:12px;line-height:17px;margin-top:14px}

/* commitment */
.photo{left:147px;top:1548px;width:409px;height:405px;border-radius:16px;background:linear-gradient(135deg,#c9c2b6,#8fa3b5 55%,#e6e8ea)}
.commit h2{left:603px;top:1543px;width:460px;font-size:36px;line-height:41px;color:var(--ink)}
.commit .body{left:603px;top:1725px;width:445px;font-size:12.4px;line-height:17.3px;text-align:justify}

/* team */
.team{position:absolute;left:0;top:2015px;width:1200px;height:658px;background:var(--mint)}
.team h2{position:absolute;width:1200px;top:50px;text-align:center;font-size:37px}
.member{position:absolute;top:175px;width:200px;text-align:center}
.member .avatar{width:193px;height:193px;border-radius:50%;background:var(--team);margin:0 auto}
.member h3{font-family:"Outfit",sans-serif;font-weight:700;font-size:17px;margin-top:28px}
.member .role{font-size:16px;font-weight:300;margin-top:2px}
.member p{font-size:12.4px;line-height:17.4px;margin-top:8px}
.member .btn{display:inline-flex;width:92px;height:35px;border-radius:18px;background:var(--green);color:var(--white);font-size:12px;font-weight:600;align-items:center;justify-content:center;margin-top:16px}

/* footer */
.footer{position:absolute;left:0;top:2673px;width:1200px;height:698px;background:linear-gradient(180deg,var(--navy-deep),#0d3050 60%,var(--navy-deep));color:var(--white)}
.follow{position:absolute;left:853px;top:64px;font-family:"Outfit",sans-serif;font-weight:700;font-size:12px}
.social{position:absolute;top:60px;width:21px;height:21px;border-radius:50%;border:2px solid var(--white)}
.col{position:absolute;top:142px;font-size:11.4px;line-height:15.7px}
.col h4{font-family:"Outfit",sans-serif;font-weight:700;font-size:12.5px;margin-bottom:10px}
.col .gap{height:16px}
.tagline{position:absolute;left:765px;top:556px;font-size:11.5px;font-weight:500}
.fline{position:absolute;left:189px;top:577px;width:761px;height:2px;background:var(--green)}
.legal{position:absolute;left:0;width:1200px;top:603px;text-align:center;font-size:8.6px;line-height:14px}
.copy{position:absolute;left:0;width:1200px;top:648px;text-align:center;font-size:11px;font-weight:300}
</style>
</head>
<body>

<header class="hero">
  <div class="hero-wave" role="img" aria-label="Green dotted wave pattern"></div>
  <div class="brand abs" style="left:148px;top:26px"><i></i>corvanta</div>
  <nav class="nav">
    <span style="left:332px">Home</span>
    <span style="left:404px">How it Works</span>
    <span style="left:526px">Products</span>
    <span style="left:621px">FAQs</span>
    <span style="left:690px">About</span>
  </nav>
  <div class="cta">Choose a Product</div>
  <div class="login">Login</div>
  <h1 class="head">About <span class="accent">Us</span></h1>
  <p>Lorem ipsum dolor sit amet, consectetur adipiscing elit, sed do eiusmod<br>tempor incididunt ut labore et dolore magna aliqua</p>
</header>

<section class="about">
  <h2 class="abs head">About <span class="accent">Us</span></h2>
  <div class="rule" style="left:148px;top:563px"></div>
  <p class="abs body">Sed ut perspiciatis unde omnis iste natus error sit voluptatem accusantium doloremque laudantium, totam rem aperiam, eaque ipsa quae ab illo inventore veritatis et quasi architecto beatae vitae dicta sunt explicabo. Nemo enim ipsam voluptatem quia voluptas sit aspernatur aut odit aut fugit, sed quia consequuntur magni dolores eos qui ratione voluptatem sequi nesciunt. Neque porro quisquam est, qui dolorem ipsum quia dolor sit amet, consectetur, adipisci velit, sed quia non numquam eius modi tempora incidunt ut labore et dolore magnam aliquam quaerat voluptatem. Ut enim ad minima veniam, quis nostrum exercitationem ullam corporis suscipit laboriosam, nisi ut aliquid ex ea commodi consequatur? Quis autem vel eum iure reprehenderit qui in ea voluptate velit esse quam nihil molestiae consequatur, vel illum qui dolorem eum fugiat quo voluptas nulla paria.</p>
  <div class="card" style="left:148px">
    <svg width="48" height="48" viewBox="0 0 48 48"><circle cx="22" cy="26" r="19" fill="none" stroke="#22c074" stroke-width="5"/><circle cx="22" cy="26" r="9" fill="none" stroke="#22c074" stroke-width="4"/><circle cx="22" cy="26" r="3" fill="#22c074"/><path d="M24 24 L42 6 M36 5 L43 5 L43 12" stroke="#22c074" stroke-width="3" fill="none"/></svg>
    <h3>Mission</h3>
    <p>Sed ut perspiciatis unde omnis iste natus error sit voluptatem accusantium doloremque laudantium, totam rem aperiam, eaque ipsa quae ab illo inventore veritatis et quasi .</p>
  </div>
  <div class="card" style="left:433px">
    <svg width="50" height="44" viewBox="0 0 50 44"><path d="M3 24 Q25 4 47 24 Q25 44 3 24Z" fill="none" stroke="#22c074" stroke-width="4"/><circle cx="25" cy="24" r="7" fill="#22c074"/><path d="M25 2v6M12 5l3 5M38 5l-3 5M4 11l4 3M46 11l-4 3" stroke="#22c074" stroke-width="3"/></svg>
    <h3>Vision</h3>
    <p>Sed ut perspiciatis unde omnis iste natus error sit voluptatem accusantium doloremque laudantium, totam rem aperiam, eaque ipsa quae ab illo inventore veritatis et quasi .</p>
  </div>
  <div class="abs mark" role="img" aria-label="Large brand mark decoration"></div>
</section>

<section class="values">
  <h2 class="head">Our <span class="accent">Values</span></h2>
  <div class="rule" style="left:574px;top:119px"></div>
  <div class="value" style="left:138px">
    <div class="ic"><svg width="40" height="40" viewBox="0 0 40 40"><circle cx="20" cy="20" r="16" fill="none" stroke="#fff" stroke-width="2.5"/><text x="20" y="27" text-anchor="middle" font-size="20" fill="#fff" font-family="Poppins,sans-serif">£</text></svg></div>
    <h3>Lorem Ipsum</h3>
    <p>Sed ut perspiciatis unde omnis iste natus error sit voluptatem accusantium doloremque laudantium</p>
  </div>
  <div class="value" style="left:370px">
    <div class="ic"><svg width="40" height="40" viewBox="0 0 40 40"><path d="M20 6l9 4v7c0 6-4 10-9 12-5-2-9-6-9-12v-7z" fill="none" stroke="#fff" stroke-width="2.5"/><path d="M4 26l8 8h6M36 26l-8 8h-6" fill="none" stroke="#fff" stroke-width="2.5"/></svg></div>
    <h3>Lorem Ipsum</h3>
    <p>Sed ut perspiciatis unde omnis iste natus error sit voluptatem accusantium doloremque laudantium</p>
  </div>
  <div class="value" style="left:617px">
    <div class="ic"><svg width="40" height="40" viewBox="0 0 40 40"><circle cx="20" cy="20" r="8" fill="none" stroke="#fff" stroke-width="3"/><circle cx="20" cy="20" r="14" fill="none" stroke="#fff" stroke-width="3" stroke-dasharray="5 4"/></svg></div>
    <h3>Lorem Ipsum</h3>
    <p>Sed ut perspiciatis unde omnis iste natus error sit voluptatem accusantium doloremque laudantium</p>
  </div>
  <div class="value" style="left:865px">
    <div class="ic"><svg width="40" height="40" viewBox="0 0 40 40"><rect x="9" y="6" width="18" height="24" rx="2" fill="none" stroke="#fff" stroke-width="2.5"/><path d="M13 12h10M13 17h10M13 22h6" stroke="#fff" stroke-width="2"/><circle cx="28" cy="28" r="6" fill="#22c074" stroke="#fff" stroke-width="2.5"/><path d="M25 28l2 2 4-4" stroke="#fff" stroke-width="2" fill="none"/></svg></div>
    <h3>Lorem Ipsum</h3>
    <p>Sed ut perspiciatis unde omnis iste natus error sit voluptatem accusantium doloremque laudantium</p>
  </div>
</section>

<section class="commit">
  <div class="abs photo" role="img" aria-label="Photo of hands signing an insurance document"></div>
  <h2 class="abs head"><span class="accent">Corvanta’s commitment</span> to innovation and its role in the insurance market.</h2>
  <div class="rule" style="left:603px;top:1693px"></div>
  <p class="abs body">Sed ut perspiciatis unde omnis iste natus error sit voluptatem accusantium doloremque laudantium, totam rem aperiam, eaque ipsa quae ab illo inventore veritatis et quasi architecto beatae vitae dicta sunt explicabo. Nemo enim ipsam voluptatem quia voluptas sit aspernatur aut odit aut fugit, sed quia consequuntur magni dolores eos qui ratione voluptatem sequi nesciunt. Neque porro quisquam est, qui dolorem ipsum quia dolor sit amet, consectetur, adipisci velit, sed quia non numquam eius modi tempora incidunt ut labore et dolore magnam aliquam quaerat voluptatem. Ut enim ad minima veniam, quis nostrum exercitationem ullam corporis suscipit laboriosam, nisi ut aliquid ex ea commodi consequatur? Quis autem vel eum iure reprehenderit qui in ea voluptate velit esse quam nihil molestiae consequatur, vel illum qui dolorem eum fugiat quo voluptas nulla paria.</p>
</section>

<section class="team">
  <h2 class="head">Our <span class="accent">Team</span></h2>
  <div class="rule" style="left:574px;top:112px"></div>
  <div class="member" style="left:145px"><div class="avatar" role="img" aria-label="Team member portrait"></div><h3>Richard</h3><div class="role">Manager</div><p>Sed ut perspiciatis unde omnis iste natus error sit voluptatem accusantium doloremque laud antium, totam rem aperiam, eaque ipsa quae</p><span class="btn">View Bio</span></div>
  <div class="member" style="left:380px"><div class="avatar" role="img" aria-label="Team member portrait"></div><h3>Richard</h3><div class="role">Manager</div><p>Sed ut perspiciatis unde omnis iste natus error sit voluptatem accusantium doloremque laud antium, totam rem aperiam, eaque ipsa quae</p><span class="btn">View Bio</span></div>
  <div class="member" style="left:615px"><div class="avatar" role="img" aria-label="Team member portrait"></div><h3>Richard</h3><div class="role">Manager</div><p>Sed ut perspiciatis unde omnis iste natus error sit voluptatem accusantium doloremque laud antium, totam rem aperiam, eaque ipsa quae</p><span class="btn">View Bio</span></div>
  <div class="member" style="left:855px"><div class="avatar" role="img" aria-label="Team member portrait"></div><h3>Richard</h3><div class="role">Manager</div><p>Sed ut perspiciatis unde omnis iste natus error sit voluptatem accusantium doloremque laud antium, totam rem aperiam, eaque ipsa quae</p><span class="btn">View Bio</span></div>
</section>

<footer class="footer">
  <div class="brand abs" style="left:148px;top:40px"><i></i>corvanta</div>
  <div class="follow">Follow us</div>
  <span class="social" style="left:932px"></span>
  <span class="social" style="left:963px"></span>
  <span class="social" style="left:994px"></span>
  <span class="social" style="left:1025px"></span>
  <div class="col" style="left:149px">
    <h4>United Kingdom Office</h4>
    Fernhill House, 14 Larch Lane,<br>Ashbury, Westshire, United<br>Kingdom, AB12 3CD
    <div class="gap"></div>
    Email Address:<br>hello@corvanta-example.co.uk
  </div>
  <div class="col" style="left:380px">
    <h4>Services</h4>
    All Services<br>Staffing Services<br>Direct Placement<br>Executive Recruiting<br>Recruitment Process Outsourcing (RPO)<br>Meadowline Professional Services<br>Harbourview Culture Consulting<br>Hire Someone
  </div>
  <div class="col" style="left:641px">
    <h4>Resources</h4>
    Consultants<br>Find a Job<br>Time &amp; Expense Approval<br>Timesheet Printout<br>Employment Verification<br>In-House Team<br>Team Shop<br>Join Our In-House Team<br>Open Doors Roadshow<br>Job Index
    <div class="gap" style="height:26px"></div>
    <h4>Partnerships</h4>
    Join our providers panel<br>Affiliates<br>Research &amp; Development Partner
  </div>
  <div class="col" style="left:846px">
    <h4>Information</h4>
    About<br>ESG<br>Veterans<br>Blog<br>Newsroom<br>Contact<br>Office Locations<br>Complete Guides<br>Videos &amp; Events<br>Resources<br>Privacy Policy<br>Workforce Privacy Policy<br>Regional Accessibility Policy<br>Do Not Sell or Share My Personal Info<br>Consumer Rights Request<br>Transparency in Coverage<br>Terms of Use<br>Sitemap<br>Corporate Ethics Hotline<br>Anti-Racism Statement<br>Compliance Program Policies<br>Consumer Alerts
  </div>
  <div class="tagline">Insurance The <span class="accent">Corvanta</span> Way!</div>
  <div class="fline"></div>
  <p class="legal">Corvanta is a trading style of Northvale Holdings Limited who are a registered company in England and Wales. Registered number: 00000000.<br>Authorised and regulated by the financial regulator under Firm Reference Number 000000. This can be checked on the public register at www.regulator-example.org/register.</p>
  <p class="copy">Copyright © 2025 All Rights Reserved</p>
</footer>

</body>
</html>
```